Yukisaro Sports Company Business Card and Logo Design

We need a business card design for a new company based in Tokyo. Our company is the first e-commerce business to sell Japanese baseball apparel to the English speaking market. We have 3 of the 12 Japanese teams on board with us at the moment. Although we will be starting with baseball we will venture into other sports as well. The name of the company is "yukisaro" sports. Yukisaro means - a bridge connecting two sides with differences, such as people, countries, and cultures. We would like our bridge to promote apparel. I would like a slick,modern design(business card) that screams "wow" the minute one sees it.

Industry/Entity Type

Business

Contact Information for Business Card

Nagisaro RW Bldg. 4F
3-8-22 Nagisaro, Minato-ku
Tokyo, Japan 108-0097

Font styles to use
Serif

```html
<!DOCTYPE html>
<html lang="en">
<head>
<meta charset="utf-8">
<title>Yukisaro Sports Company – Business Card</title>
<link rel="stylesheet" href="https://fonts.googleapis.com/css2?family=Lora:wght@400;500&display=swap">
<style>
  :root {
    --backdrop: #d9d8d6;
    --card: #fbfbfa;
    --ink: #3a3a3c;
    --ink-soft: #4a4a4c;
    --accent: #f2b634;
    --shadow: rgba(0, 0, 0, 0.18);
  }
  * { margin: 0; padding: 0; box-sizing: border-box; }
  html, body {
    width: 798px;
    height: 1200px;
    overflow: hidden;
    background: var(--backdrop);
  }
  .canvas {
    width: 798px;
    height: 1200px;
    display: flex;
    align-items: center;
    justify-content: center;
  }
  .business-card {
    width: 680px;
    height: 390px;
    background: var(--card);
    box-shadow: 0 18px 40px var(--shadow);
    display: flex;
    flex-direction: column;
    align-items: center;
    justify-content: center;
    font-family: "Lora", Georgia, serif;
    color: var(--ink);
  }
  .brand {
    display: flex;
    flex-direction: column;
    align-items: center;
  }
  .brand-dot {
    width: 58px;
    height: 58px;
    border-radius: 50%;
    background: var(--accent);
    margin-bottom: 12px;
  }
  .brand-name {
    font-size: 50px;
    font-weight: 400;
    letter-spacing: 1px;
    line-height: 1;
    color: var(--ink);
  }
  .brand-tagline {
    margin-top: 6px;
    font-size: 17px;
    font-weight: 400;
    letter-spacing: 8px;
    padding-left: 8px;
    line-height: 1.2;
    text-transform: lowercase;
    color: var(--accent);
  }
  .address {
    margin-top: 22px;
    font-style: normal;
    text-align: center;
    font-size: 15px;
    font-weight: 500;
    line-height: 1.45;
    color: var(--ink-soft);
  }
</style>
</head>
<body>
  <main class="canvas">
    <section class="business-card">
      <div class="brand">
        <span class="brand-dot"></span>
        <span class="brand-name">yukisaro</span>
        <span class="brand-tagline">sports</span>
      </div>
      <address class="address">
        Nagisaro RW Bldg. 4F<br>
        3-8-22 Nagisaro, Minato-ku<br>
        Tokyo, Japan 108-0097
      </address>
    </section>
  </main>
</body>
</html>
```